Landing page for a sports website

we have a sports tracking and management website and require a web site.
the site should have the ability to have 2 options for selection the first being a competitions portal the other a club portal there should be a about us page and a contact us page
the site should be dynamic and vibrant and be easily recognisable as a multiple sports page
we also have www.velorinote.com and would like it to compliment that site
i would like to have some form of animation regarding sports occur when you click the login option if that is possible
the site is www.vlnsports.com and I have attached the logo in both 3d and standard
we also require a design several templates for information pages please see www.tallyhusk.com as an example of how it should look but with a sports theme
Target Market(s)
This will be used for primarily team based sports
Industry/Entity Type
Management
Number of Pages Required
3 page
Requirements
Must have
- the ability to change the logo and names of the site
- i.e. from vlnsports to vlnschools at a later date

```html
<!DOCTYPE html>
<html lang="en">
<head>
<meta charset="utf-8">
<title>VLN Sports</title>
<link rel="stylesheet" href="https://fonts.googleapis.com/css2?family=Anton&family=Arimo:wght@400;700&display=swap">
<style>
  :root {
    --page-black: #050607;
    --bar-grey: #1b1e21;
    --athlete-teal: #2f6a80;
    --athlete-deep: #173642;
    --footer-top: #1d2328;
    --footer-bottom: #3b4b56;
    --link-teal: #2c7d99;
    --copy-teal: #3b8fae;
    --brand-blue: #3a9fc6;
    --button-blue: #4aaed6;
    --button-light: #e4e6e8;
    --portal-fill: rgba(205, 208, 211, 0.72);
    --ink: #0e1012;
  }
  * { margin: 0; padding: 0; box-sizing: border-box; }
  html, body { width: 1200px; height: 675px; overflow: hidden; background: var(--page-black); }
  .page {
    position: relative; width: 1200px; height: 675px; overflow: hidden;
    font-family: "Arimo", Arial, sans-serif;
  }
  .hero {
    position: absolute; left: 0; top: 0; width: 1200px; height: 306px;
    background: linear-gradient(180deg, var(--page-black) 0%, #07090a 60%, #121618 100%);
  }
  .hero-artwork {
    position: absolute; left: 0; top: 45px; width: 1200px; height: 225px;
    background:
      radial-gradient(ellipse 110px 70px at 120px 140px, rgba(47, 106, 128, 0.75), transparent 75%),
      radial-gradient(ellipse 90px 70px at 270px 100px, rgba(47, 106, 128, 0.7), transparent 75%),
      radial-gradient(ellipse 90px 60px at 380px 95px, rgba(47, 106, 128, 0.65), transparent 75%),
      radial-gradient(ellipse 80px 60px at 560px 100px, rgba(47, 106, 128, 0.6), transparent 75%),
      radial-gradient(ellipse 90px 55px at 740px 55px, rgba(47, 106, 128, 0.7), transparent 75%),
      radial-gradient(ellipse 110px 55px at 870px 75px, rgba(47, 106, 128, 0.75), transparent 75%),
      radial-gradient(ellipse 60px 80px at 1000px 75px, rgba(47, 106, 128, 0.7), transparent 75%),
      radial-gradient(ellipse 80px 60px at 1020px 175px, rgba(47, 106, 128, 0.55), transparent 75%),
      radial-gradient(ellipse 50px 90px at 1110px 135px, rgba(47, 106, 128, 0.7), transparent 75%),
      linear-gradient(180deg, var(--athlete-deep) 0%, #0d1c22 60%, rgba(10, 14, 16, 0) 100%);
  }
  .top-bar {
    position: absolute; left: 0; top: 22px; width: 1200px; height: 23px;
    background: var(--bar-grey);
  }
  .mini-brand {
    position: absolute; left: 71px; top: 24px;
    font-weight: 700; font-size: 17px; color: #f2f2f2; letter-spacing: 0.5px;
  }
  .brand {
    position: absolute; left: 422px; top: 14px; width: 284px; text-align: center;
    font-family: "Anton", Impact, sans-serif; font-size: 52px; line-height: 64px;
    color: var(--brand-blue); letter-spacing: 2px;
  }
  .auth-button {
    position: absolute; top: 22px; height: 23px; border-radius: 5px;
    font-family: "Anton", Impact, sans-serif; font-size: 16px; line-height: 23px;
    text-align: center; color: var(--ink); text-decoration: none;
  }
  .auth-button.sign-up { left: 948px; width: 77px; background: linear-gradient(180deg, #6cc3e6, var(--button-blue)); }
  .auth-button.sign-in { left: 1046px; width: 77px; background: var(--button-light); }
  .portal {
    position: absolute; top: 201px; height: 49px;
    background: var(--portal-fill);
    font-family: "Anton", Impact, sans-serif; font-size: 40px; line-height: 49px;
    color: var(--ink); text-align: center; text-decoration: none;
  }
  .portal.competitions { left: 195px; width: 405px; }
  .portal.clubs { left: 625px; width: 275px; }
  .footer {
    position: absolute; left: 0; top: 306px; width: 1200px; height: 369px;
    background: linear-gradient(180deg, var(--footer-top) 0%, var(--footer-bottom) 100%);
    color: var(--link-teal);
  }
  .legal { position: absolute; left: 37px; top: 42px; font-size: 15px; line-height: 18.5px; }
  .legal a, .footer-links a, .contact-links a { color: var(--link-teal); text-decoration: none; display: block; }
  .footer-heading { position: absolute; font-size: 22px; font-weight: 400; }
  .read-more { left: 240px; top: 30px; }
  .contact { left: 986px; top: 30px; }
  .footer-links { position: absolute; left: 240px; top: 78px; font-size: 18px; line-height: 22.5px; list-style: none; }
  .contact-links { position: absolute; left: 986px; top: 70px; font-size: 15px; line-height: 18.5px; list-style: none; }
  .about-copy {
    position: absolute; left: 415px; top: 28px; width: 462px;
    font-size: 14.3px; line-height: 18px; color: var(--copy-teal);
    text-align: left; hyphens: auto; -webkit-hyphens: auto;
  }
</style>
</head>
<body>
<div class="page">
  <header class="hero">
    <div class="hero-artwork" role="img" aria-label="Teal silhouettes of athletes from many sports: skiing, cycling, motocross, skating, gymnastics and football"></div>
    <div class="top-bar"></div>
    <div class="mini-brand">VLN</div>
    <div class="brand">VLN SPORTS</div>
    <a class="auth-button sign-up" href="#">SIGN UP</a>
    <a class="auth-button sign-in" href="#">SIGN IN</a>
    <a class="portal competitions" href="#">COMPETITIONS PORTAL</a>
    <a class="portal clubs" href="#">CLUBS PORTAL</a>
  </header>
  <footer class="footer">
    <div class="legal">
      <span>© VLN Sports Inc 2015</span>
      <a href="#">Terms of Service</a>
      <a href="#">Privacy Policy</a>
    </div>
    <h3 class="footer-heading read-more">Read more</h3>
    <ul class="footer-links">
      <li><a href="#">Features</a></li>
      <li><a href="#">Pricing</a></li>
      <li><a href="#">About</a></li>
      <li><a href="#">Blog</a></li>
      <li><a href="#">Status</a></li>
      <li><a href="#">API</a></li>
      <li><a href="#">Integrations</a></li>
      <li><a href="#">Jobs</a></li>
    </ul>
    <p class="about-copy" lang="en">"Sed ut perspiciatis unde omnis iste natus error sit voluptatem accusantium doloremque laudantium, totam rem aperiam, eaque ipsa quae ab illo inventore veritatis et quasi architecto beatae vitae dicta sunt explicabo. Nemo enim ipsam voluptatem quia voluptas sit aspernatur aut odit aut fugit, sed quia consequuntur magni dolores eos qui ratione voluptatem sequi nesciunt. Neque porro quisquam est, qui dolorem ipsum quia dolor sit amet, consectetur, adipisci velit, sed quia non numquam eius modi tempora incidunt ut labore et dolore magnam aliquam quaerat voluptatem. Ut enim ad minima veniam, quis nostrum exercitationem ullam corporis suscipit laboriosam, nisi ut aliquid ex ea commodi consequatur? Quis autem vel eum iure reprehenderit qui in ea voluptate velit esse quam nihil molestiae consequatur, vel illum qui dolorem eum fugiat quo voluptas nulla pariatur?"</p>
    <h3 class="footer-heading contact">Contact Us</h3>
    <ul class="contact-links">
      <li><a href="#">Contact</a></li>
      <li><a href="#">Support</a></li>
    </ul>
  </footer>
</div>
</body>
</html>
```